依頼詳細
今回はコーポレートサイトのTOPページのデザインをお願いしたく思います。

【素材】
素材に関しては、ロゴや写真等は現在準備中でして、
デザインの際は仮のオブジェクトを入れて対応して頂ければと思います。

【サイト構成】
サイトの構成については、ラフを書きましたので下記URLからダウンロードお願いします。
http://qlvd.jp/RmWoPa

※PCを想定したデザインでお願いいたします。

【イメージ】
以下が現在の「ソラミネ不動産株式会社」のコーポレートサイトになります。
http://www.aobane-juhan.co.jp/

今回ご提案いただく新しいサイトのデザインは上記のものから一新して

1.スタイリッシュ
2.NY
3.最先端
4.近未来
5.エネルギッシュ
6.エキサイティング
7.自由
8.それでいてシンプル

なイメージ、従来の不動産会社のイメージに囚われないものにしたく思います。

【参考サイト】
https://www.kazemura-lab.co.jp/

ページ数
1ページ
希望イメージ
シンプル 複雑
単色 カラフル
暗い 明るい
日常 高級
遊び心 厳粛
未来的 伝統的
女性的 男性的
希望する色
グレー系
補足説明
今回のデザインで採用させて頂いた方には、
コーポレートサイトの「代表メッセージ」「ニュース」「投資実績」の他3ページのデザインやコーディングなど、他のお仕事に関してもご相談させて頂ければと思います。
(もちろん当案件のみご希望の方からも募集しており、採用有無には関係ありません。)
■ 選んだ理由

色のコンセプトと対応の早さ、デザインの良さで決定致しました。

■ 提案者全員のお礼・コメント

皆さま、お忙しい所多くのご提案を頂きまして誠にありがとうございます。
また何かございましたらお願いをさせて頂きますので引き続き宜しくお願い致します。

```html
<!DOCTYPE html>
<html lang="ja">
<head>
<meta charset="UTF-8">
<title>SORAMINE | ソラミネ不動産株式会社</title>
<link rel="stylesheet" href="https://fonts.googleapis.com/css2?family=Montserrat:wght@400;500;600;700&family=Noto+Sans+JP:wght@400;500;700&display=swap">
<style>
:root{
  --navy:#1b3a7a;
  --navy-deep:#132c60;
  --blue:#2a57a8;
  --ink:#333a44;
  --muted:#7d8592;
  --paper:#f1f3f7;
  --line:#cfd5de;
  --white:#ffffff;
}
*{margin:0;padding:0;box-sizing:border-box}
html,body{width:1200px;height:2728px;overflow:hidden}
body{font-family:"Noto Sans JP",sans-serif;color:var(--ink);background:var(--paper)}
.page{position:relative;width:1200px;height:2728px;overflow:hidden;
  background:linear-gradient(160deg,#f6f7fa 0%,#e9edf3 40%,#f4f6f9 60%,#e4e9f1 100%)}
.abs{position:absolute}

/* header */
.menu-btn{left:0;top:0;width:56px;height:72px;background:var(--navy);color:var(--white);
  display:flex;flex-direction:column;align-items:center;justify-content:center;gap:5px;z-index:3}
.menu-btn span{display:block;width:22px;height:2px;background:var(--white)}
.menu-btn small{font-family:"Montserrat",sans-serif;font-size:8px;letter-spacing:1px;margin-top:3px}
.global-nav{right:152px;top:0;height:72px;display:flex;align-items:center;gap:44px;z-index:3}
.global-nav a{font-family:"Montserrat",sans-serif;font-size:13px;font-weight:600;letter-spacing:1.5px;color:var(--white);text-decoration:none}
.contact-btn{right:0;top:0;width:140px;height:72px;background:var(--navy);color:var(--white);
  display:flex;align-items:center;justify-content:center;font-family:"Montserrat",sans-serif;font-size:13px;font-weight:600;letter-spacing:1.5px;z-index:3}

/* hero */
.hero{left:0;top:0;width:1200px;height:688px;
  background:linear-gradient(180deg,#9fb2cc 0%,#6f88ac 35%,#3f5b86 70%,#2c4670 100%)}
.hero-title{left:0;top:300px;width:1200px;text-align:center;font-family:"Montserrat",sans-serif;
  font-weight:500;font-size:112px;letter-spacing:14px;color:var(--white)}

/* section labels */
.label{font-family:"Montserrat",sans-serif;font-weight:700;font-size:22px;letter-spacing:2px;color:var(--navy)}
.label::after{content:"";display:block;width:28px;height:3px;background:var(--navy);margin-top:8px}

/* philosophy */
.philo-head{left:160px;top:900px;width:270px;font-size:30px;font-weight:700;line-height:1.55;color:var(--blue);white-space:nowrap;z-index:2}
.philo-text{left:160px;top:1060px;width:240px;font-size:12px;line-height:2;color:var(--ink)}
.philo-block{left:440px;top:896px;width:110px;height:124px;background:var(--navy)}
.philo-photo{left:530px;top:940px;width:500px;height:300px;
  background:linear-gradient(120deg,#dfe3ea 0%,#b7c0cd 50%,#8a97a9 100%)}

/* work */
.work-card{top:1432px;width:272px}
.work-photo{width:272px;height:160px}
.work-tag{position:absolute;left:0;top:148px;background:var(--navy);color:var(--white);
  font-family:"Montserrat",sans-serif;font-size:11px;font-weight:600;letter-spacing:1px;padding:4px 10px}
.work-meta{margin-top:20px;font-size:11px;line-height:1.8;color:var(--ink)}
.work-meta dt{display:inline-block;width:60px;color:var(--muted)}
.work-meta dd{display:inline}
.more-btn{left:530px;top:1702px;width:140px;height:34px;border-radius:17px;background:var(--navy);color:var(--white);
  display:flex;align-items:center;justify-content:center;font-family:"Montserrat",sans-serif;font-size:11px;letter-spacing:1.5px}

/* profile */
.profile-panel{left:420px;top:1840px;width:620px;height:340px;background:var(--navy);padding:36px 30px;
  display:flex;gap:30px;color:var(--white)}
.profile-table{border-collapse:collapse;font-size:11px;line-height:1.7}
.profile-table th{text-align:left;font-weight:500;width:70px;padding:7px 0;vertical-align:top;border-bottom:1px solid rgba(255,255,255,.25)}
.profile-table td{padding:7px 0;border-bottom:1px solid rgba(255,255,255,.25);vertical-align:top}
.map{left:160px;top:1928px;width:268px;height:384px;background:linear-gradient(135deg,#eceff2,#d9dee4)}

/* news */
.news{left:440px;top:2180px;width:600px;height:320px;background:var(--white);padding:34px 40px}
.news-title{font-family:"Montserrat",sans-serif;font-weight:700;font-size:20px;letter-spacing:2px;color:var(--navy)}
.news-list{list-style:none;margin-top:26px;width:340px}
.news-list li{font-size:11px;padding:12px 0;border-bottom:1px solid var(--line);display:flex;gap:18px}
.news-list time{font-family:"Montserrat",sans-serif;color:var(--muted)}
.inquiry-btn{right:40px;top:80px;width:136px;height:36px;border:1px solid var(--navy);color:var(--navy);
  display:flex;align-items:center;justify-content:center;gap:8px;font-size:11px;font-weight:500}

/* footer */
.footer{left:0;top:2528px;width:1200px;height:200px;background:var(--navy)}
.pagetop{left:576px;top:2508px;width:48px;height:24px;background:var(--navy);border-radius:24px 24px 0 0;
  display:flex;align-items:center;justify-content:center}
.footer-logo{left:160px;top:2620px;font-family:"Montserrat",sans-serif;font-weight:500;font-size:32px;letter-spacing:4px;color:var(--white)}
.footer-addr{left:160px;top:2670px;font-size:9px;opacity:.8;color:var(--white)}
.footer-nav{right:160px;top:2630px;display:flex;gap:14px;font-family:"Montserrat",sans-serif;font-weight:600;font-size:16px;letter-spacing:2px;color:var(--white)}
.copyright{right:160px;top:2670px;font-family:"Montserrat",sans-serif;font-size:9px;opacity:.8;color:var(--white)}
</style>
</head>
<body>
<div class="page">

  <header>
    <div class="abs menu-btn"><span></span><span></span><span></span><small>MENU</small></div>
    <nav class="abs global-nav"><a>ABOUT</a><a>WORK</a><a>NEWS</a></nav>
    <div class="abs contact-btn">CONTACT</div>
  </header>

  <section>
    <div class="abs hero" role="img" aria-label="ニューヨークの高層ビル街の写真"></div>
    <h1 class="abs hero-title">SORAMINE</h1>
  </section>

  <section>
    <h2 class="abs label" style="left:160px;top:800px">PHILOSOPHY</h2>
    <p class="abs philo-head">不動産の<br>新しい未来をつくる</p>
    <p class="abs philo-text">この文章はダミーです。文字の大きさ、量、字間、行間等を確認するために入れています。この文章はダミーです。<br>文字の大きさ、量、字間、行間等を確認するために入れています。<br>この文章はダミーです。文字の大きさ、量、字間、行間等を確認するために入れています。</p>
    <div class="abs philo-block"></div>
    <div class="abs philo-photo" role="img" aria-label="近代的な集合住宅の外観写真"></div>
  </section>

  <section>
    <h2 class="abs label" style="left:160px;top:1340px">WORK</h2>

    <article class="abs work-card" style="left:160px">
      <div class="work-photo" role="img" aria-label="夜景に映える邸宅の写真" style="background:linear-gradient(135deg,#5b4a3c,#c79a62 55%,#2f3540)"></div>
      <span class="work-tag">FUKUOKA 01</span>
      <dl class="work-meta"><dt>所在地</dt><dd>福岡市中央区</dd><br><dt>竣工</dt><dd>2017年</dd><br><dt>用途</dt><dd>戸建住宅</dd></dl>
    </article>
    <article class="abs work-card" style="left:464px">
      <div class="work-photo" role="img" aria-label="白い外壁の住宅群の写真" style="background:linear-gradient(135deg,#c9d3de,#eef1f4 50%,#8d9aab)"></div>
      <span class="work-tag">FUKUOKA 02</span>
      <dl class="work-meta"><dt>所在地</dt><dd>福岡市博多区</dd><br><dt>竣工</dt><dd>2016年</dd><br><dt>用途</dt><dd>集合住宅</dd></dl>
    </article>
    <article class="abs work-card" style="left:768px">
      <div class="work-photo" role="img" aria-label="青空の下のモダン住宅の写真" style="background:linear-gradient(180deg,#9cc0e2,#e6e7e3 60%,#a0a48c)"></div>
      <span class="work-tag">FUKUOKA 03</span>
      <dl class="work-meta"><dt>所在地</dt><dd>福岡市早良区</dd><br><dt>竣工</dt><dd>2015年</dd><br><dt>用途</dt><dd>戸建住宅</dd></dl>
    </article>

    <div class="abs more-btn">VIEW MORE</div>
  </section>

  <section>
    <h2 class="abs label" style="left:160px;top:1840px">PROFILE</h2>
    <div class="abs map" role="img" aria-label="本社所在地の地図"></div>
    <div class="abs profile-panel">
      <table class="profile-table" style="width:300px">
        <tr><th>会社名</th><td>ソラミネ不動産株式会社</td></tr>
        <tr><th>所在地</th><td>福岡市中央区青葉町1-2-3<br>ソラミネビル5F</td></tr>
        <tr><th>設立</th><td>平成10年4月</td></tr>
        <tr><th>資本金</th><td>1,000万円</td></tr>
        <tr><th>事業内容</th><td>不動産の売買・賃貸・仲介<br>不動産の管理業務<br>建築工事の企画・設計</td></tr>
      </table>
      <table class="profile-table" style="width:230px">
        <tr><th>代表者</th><td>代表取締役</td></tr>
        <tr><th>従業員数</th><td>25名</td></tr>
        <tr><th>取引銀行</th><td>青葉銀行 本店<br>中央信用金庫 支店</td></tr>
        <tr><th>免許</th><td>宅地建物取引業免許<br>福岡県知事（3）</td></tr>
      </table>
    </div>

    <div class="abs news">
      <h2 class="news-title">NEWS</h2>
      <ul class="news-list">
        <li><time>2017.08.01</time><span>ウェブサイトをリニューアルしました。</span></li>
        <li><time>2017.07.15</time><span>ウェブサイトをリニューアルしました。</span></li>
        <li><time>2017.07.01</time><span>ウェブサイトをリニューアルしました。</span></li>
      </ul>
      <div class="abs inquiry-btn">
        <svg width="14" height="10" viewBox="0 0 14 10"><rect x="0.5" y="0.5" width="13" height="9" fill="none" stroke="currentColor"/><path d="M0.5 0.5 L7 5.5 L13.5 0.5" fill="none" stroke="currentColor"/></svg>
        お問い合わせ
      </div>
    </div>
  </section>

  <footer>
    <div class="abs footer"></div>
    <div class="abs pagetop"><svg width="14" height="8" viewBox="0 0 14 8"><path d="M1 7 L7 1 L13 7" fill="none" stroke="#fff" stroke-width="1.5"/></svg></div>
    <p class="abs footer-logo">SORAMINE</p>
    <p class="abs footer-addr">〒810-0000 福岡市中央区青葉町1-2-3 ソラミネビル5F</p>
    <nav class="abs footer-nav"><span>ABOUT</span><span>/</span><span>WORK</span><span>/</span><span>NEWS</span><span>/</span><span>CONTACT</span></nav>
    <p class="abs copyright">Copyright © SORAMINE CORPORATION All Rights Reserved.</p>
  </footer>

</div>
</body>
</html>
```